New Plumbing Company

We are looking for a smart and creative business card design for our new plumbing company. We are looking for creativity and originality in our business cards.

Industry/Entity Type

Plumbing

Contact Information for Business Card

Crestline Plumbing
Peter Halvane
Managing Director
Telephone Number : 0481529604
Email : service@crestlineplumbing.com.au
Website : www.crestlineplumbing.com.au
Lic. 508264K

Colors
0692cd
33a6d7
000000

Requirements
Must have
• I want the business card to be designed on a black background using the blue tones i have selected as seen in the company logo.

```html
<!DOCTYPE html>
<html lang="en">
<head>
<meta charset="utf-8">
<title>Crestline Plumbing – Business Card</title>
<link rel="stylesheet" href="https://fonts.googleapis.com/css2?family=Didact+Gothic&display=swap">
<style>
  :root {
    --stage: #2b2624;
    --card-black: #1a1818;
    --card-blue: #2e67a8;
    --brand-blue: #0692cd;
    --brand-light: #33a6d7;
    --white: #ffffff;
    --soft-white: #e8eef6;
  }
  * { box-sizing: border-box; margin: 0; padding: 0; }
  html, body {
    width: 1200px;
    height: 768px;
    overflow: hidden;
    background: var(--stage);
    font-family: "Didact Gothic", sans-serif;
  }
  .stage {
    position: relative;
    width: 1200px;
    height: 768px;
  }
  .card {
    position: absolute;
    width: 500px;
    height: 290px;
    border-radius: 4px;
    box-shadow: 0 10px 28px rgba(0,0,0,0.45);
  }
  .card-front {
    left: 70px;
    top: 110px;
    background: var(--card-black);
    display: flex;
    align-items: center;
    justify-content: center;
  }
  .card-back {
    left: 630px;
    top: 360px;
    background: var(--card-blue);
    color: var(--white);
  }
  .brand {
    display: flex;
    align-items: center;
    gap: 14px;
  }
  .brand-dot {
    width: 34px;
    height: 34px;
    border-radius: 50%;
    border: 3px solid currentColor;
  }
  .brand-name {
    font-size: 34px;
    letter-spacing: 0.5px;
    white-space: nowrap;
  }
  .card-front .brand { color: var(--brand-light); }
  .card-back .brand {
    position: absolute;
    left: 30px;
    top: 108px;
    color: var(--white);
    gap: 10px;
  }
  .card-back .brand-dot { width: 26px; height: 26px; border-width: 2px; }
  .card-back .brand-name { font-size: 22px; }
  .holder {
    position: absolute;
    left: 262px;
    top: 78px;
  }
  .holder-name {
    font-size: 22px;
    letter-spacing: 0.5px;
  }
  .holder-title {
    font-size: 12px;
    color: var(--soft-white);
    margin-top: 2px;
  }
  .contacts {
    position: absolute;
    left: 240px;
    top: 142px;
    list-style: none;
    font-size: 13px;
    line-height: 20px;
  }
  .contacts li {
    display: flex;
    align-items: center;
    gap: 10px;
  }
  .contacts svg {
    width: 12px;
    height: 12px;
    flex: none;
    fill: var(--white);
  }
  .licence {
    position: absolute;
    left: 240px;
    top: 210px;
    font-size: 13px;
    letter-spacing: 0.5px;
  }
</style>
</head>
<body>
<main class="stage">

  <section class="card card-front" aria-label="Business card front">
    <div class="brand">
      <span class="brand-dot"></span>
      <span class="brand-name">Crestline Plumbing</span>
    </div>
  </section>

  <section class="card card-back" aria-label="Business card back">
    <div class="brand">
      <span class="brand-dot"></span>
      <span class="brand-name">Crestline Plumbing</span>
    </div>

    <div class="holder">
      <p class="holder-name">Peter Halvane</p>
      <p class="holder-title">Managing Director</p>
    </div>

    <ul class="contacts">
      <li>
        <svg viewBox="0 0 24 24" aria-hidden="true"><path d="M6.6 10.8a15.1 15.1 0 0 0 6.6 6.6l2.2-2.2a1 1 0 0 1 1-.25 11.4 11.4 0 0 0 3.6.57 1 1 0 0 1 1 1V20a1 1 0 0 1-1 1A17 17 0 0 1 3 4a1 1 0 0 1 1-1h3.5a1 1 0 0 1 1 1c0 1.25.2 2.45.57 3.57a1 1 0 0 1-.25 1z"/></svg>
        <span>0481529604</span>
      </li>
      <li>
        <svg viewBox="0 0 24 24" aria-hidden="true"><path d="M12 2a10 10 0 1 0 0 20 10 10 0 0 0 0-20zm6.9 6h-3a15.6 15.6 0 0 0-1.4-3.6A8 8 0 0 1 18.9 8zM12 4c.8 1.2 1.5 2.5 1.9 4h-3.8c.4-1.5 1.1-2.8 1.9-4zM4.3 14a8 8 0 0 1 0-4h3.4a16 16 0 0 0 0 4zm.8 2h3a15.6 15.6 0 0 0 1.4 3.6A8 8 0 0 1 5.1 16zm3-8h-3a8 8 0 0 1 4.4-3.6A15.6 15.6 0 0 0 8.1 8zM12 20c-.8-1.2-1.5-2.5-1.9-4h3.8c-.4 1.5-1.1 2.8-1.9 4zm2.3-6H9.7a14.7 14.7 0 0 1 0-4h4.6a14.7 14.7 0 0 1 0 4zm.2 5.6a15.6 15.6 0 0 0 1.4-3.6h3a8 8 0 0 1-4.4 3.6zm1.8-5.6a16 16 0 0 0 0-4h3.4a8 8 0 0 1 0 4z"/></svg>
        <span>www.crestlineplumbing.com.au</span>
      </li>
      <li>
        <svg viewBox="0 0 24 24" aria-hidden="true"><path d="M2 5h20v14H2zm2 2v.5l8 5 8-5V7zm0 2.9V17h16V9.9l-8 5z"/></svg>
        <span>service@crestlineplumbing.com.au</span>
      </li>
    </ul>

    <p class="licence">LIC. 508264K</p>
  </section>

</main>
</body>
</html>
```